Plumbing Business Card Design

our business is a plumbing business.
we would like to see designs with our LOGO featured and then either purple or black writing with a white back ground
or black back ground with white or purple writing or even a purple card!
one option we would love to see is if you could get the KTW letters away from the white background ( it is currently in a white box as a jpeg )it is currently on and overlay it onto black.
FRONT
KTW image to be displayed on the front, please use the attached picture. ( you can remove the email address and mobile number from the botttom and re write it in different font or in a different place on the front.
Directly under the large KTW we would like the words Copper Linton Plumbing.
could be spread out like this C O P P E R L I N T O N
P L U M B I N G
We really are open to suggestions though!
Also on the front of the card we could like our little catch phrase somewhere Borra's Trusted Plumber

we dont want in plumbing pictures or photos but we are open to swirl across the card or water movement or droplets.

BACK
These services need to be dot pointed or listed on the back
Hot & Cold Water Services
Gas Fitting
Bathroom & Kitchen Renovations
Metal Roofing & Guttering
New Homes & Extensions
Hot Water Service Changeovers
Drainage & Stormwater Works
All General Plumbing & Maitenance

in smaller writing or down the bottom of the card on the back please display write this Lic. No 492318

Contact Information for Business Card

Reid Linton
Mobile: 0427 316 902
email: copperlintonplumbing@mailvane.example
FInd Us on Facebook Copper Linton Plumbing ( with the f symbol ) either on the front or the back

```html
<!DOCTYPE html>
<html lang="en">
<head>
<meta charset="utf-8">
<title>Copper Linton Plumbing – Business Card</title>
<link rel="stylesheet" href="https://fonts.googleapis.com/css2?family=Open+Sans:wght@400;600;700&display=swap">
<style>
  :root {
    --backdrop: #3b3532;
    --card: #050505;
    --card-sheen: #1a1a1c;
    --blue: #1e88f5;
    --purple: #8a2be2;
    --white: #ffffff;
  }
  * { box-sizing: border-box; margin: 0; padding: 0; }
  html, body {
    width: 1200px;
    height: 844px;
    overflow: hidden;
    background: var(--backdrop);
    font-family: "Open Sans", Arial, sans-serif;
  }
  .stage {
    position: relative;
    width: 1200px;
    height: 844px;
    display: flex;
    align-items: center;
    justify-content: center;
    gap: 48px;
  }
  .card {
    position: relative;
    width: 540px;
    height: 309px;
    background: radial-gradient(ellipse at 50% 35%, var(--card-sheen) 0%, var(--card) 70%);
    color: var(--white);
    overflow: hidden;
    box-shadow: 0 14px 30px rgba(0,0,0,0.55);
  }

  /* Front */
  .card-front .band {
    position: absolute;
    left: 0;
    width: 100%;
    height: 12px;
    background: var(--blue);
  }
  .card-front .band-top { top: 10px; }
  .card-front .band-bottom { bottom: 10px; }
  .front-content {
    position: absolute;
    top: 42px;
    left: 0;
    width: 100%;
    text-align: center;
  }
  .holder-name {
    color: var(--blue);
    font-weight: 600;
    font-size: 19px;
    letter-spacing: 0.5px;
    text-transform: uppercase;
    margin-left: -60px;
  }
  .licence {
    font-size: 13px;
    margin-left: -60px;
    margin-top: 2px;
  }
  .licence-label { color: var(--purple); font-weight: 700; }

  .brand {
    display: flex;
    flex-direction: column;
    align-items: center;
    margin-top: 8px;
  }
  .brand-mark {
    display: flex;
    align-items: center;
    gap: 8px;
  }
  .brand-initials {
    color: var(--blue);
    font-weight: 700;
    font-size: 54px;
    line-height: 1;
    letter-spacing: 4px;
  }
  .brand-square {
    width: 12px;
    height: 12px;
    background: var(--purple);
  }
  .brand-name {
    color: var(--blue);
    font-weight: 700;
    font-size: 12px;
    letter-spacing: 1px;
    text-transform: uppercase;
    margin-top: 2px;
  }

  .contact {
    margin-top: 14px;
    list-style: none;
    font-size: 14px;
    line-height: 1.45;
  }

  /* Back */
  .card-back .accent {
    position: absolute;
    width: 30px;
    height: 26px;
    background: var(--blue);
    border-right: 5px solid var(--purple);
  }
  .card-back .accent-right { top: 54px; right: 0; }
  .card-back .accent-left { top: 178px; left: 0; }
  .card-back .brand { margin-top: 34px; }
  .services {
    list-style: none;
    margin-top: 20px;
    text-align: center;
    font-size: 13.5px;
    font-weight: 600;
    line-height: 1.55;
  }
  .services .divider { padding: 0 6px; font-weight: 400; }
</style>
</head>
<body>
<main class="stage">
  <section class="card card-front" aria-label="Business card front">
    <div class="band band-top"></div>
    <div class="front-content">
      <p class="holder-name">Reid Linton</p>
      <p class="licence"><span class="licence-label">Lic. No</span> 492318</p>
      <div class="brand">
        <div class="brand-mark">
          <span class="brand-initials">KTW</span>
          <span class="brand-square"></span>
        </div>
        <span class="brand-name">Copper Linton Plumbing</span>
      </div>
      <ul class="contact">
        <li>0427 316 902</li>
        <li>copperlintonplumbing@mailvane.example</li>
        <li>CopperLintonPlumbing</li>
      </ul>
    </div>
    <div class="band band-bottom"></div>
  </section>

  <section class="card card-back" aria-label="Business card back">
    <div class="accent accent-right"></div>
    <div class="accent accent-left"></div>
    <div class="brand">
      <div class="brand-mark">
        <span class="brand-initials">KTW</span>
        <span class="brand-square"></span>
      </div>
      <span class="brand-name">Copper Linton Plumbing</span>
    </div>
    <ul class="services">
      <li>Hot &amp; Cold Water Services<span class="divider">|</span>Gas Fitting</li>
      <li>Bathroom &amp; Kitchen Renovations<span class="divider">|</span>Metal Roofing &amp; Guttering</li>
      <li>New Homes &amp; Extensions<span class="divider">|</span>Hot Water Service Changeovers</li>
      <li>Drainage &amp; Stormwater Works<span class="divider">|</span>All General Plumbing &amp; Maitenance</li>
    </ul>
  </section>
</main>
</body>
</html>
```